Skyreach Pacific Aerial, a Sydney based startup need a visiting card designed

We are after a visiting card which is bold and eye catching. We are a drone company providing services and we are also Korvane authorized dealer who also sell consumer and industrial drones

Our website is under construction but you can excess from link below.

www.skyreachpacificaerial.com.au/test/

Feel free to contact me for any clarifications. we have given 5 days for the project but we are flexible to extend the project to 10 days.

Target Market(s)

Private and government organisation

Industry/Entity Type

Business Service

Contact Information for Business Card

Skyreach Pacific Aerial PTY LTD

Henrik Vollmer (Ned) ( Director)

17 Calloway Lane, Merrigum Flat, NSW 2571

Authorized Korvane Dealer

0471 238 905 / 1300Skyreachpa

info@skyreachpacificaerial.com.au

website: www.skyreachpacificaerial.com.au

Font styles to use
Serif

Requirements
Must have
• bold and stand out.
Nice to have
• colours complimenting the logo
Should not have
• not black card

```html
<!DOCTYPE html>
<html lang="en">
<head>
<meta charset="utf-8">
<title>Skyreach Pacific Aerial — Business Card</title>
<link rel="stylesheet" href="https://fonts.googleapis.com/css2?family=Open+Sans:wght@400;700;800&display=swap">
<style>
  :root {
    --page: #e8e8e8;
    --navy: #0b2038;
    --gold: #f2ad00;
    --paper: #f5f5f4;
    --ink-soft: #6c6f73;
    --white: #ffffff;
  }
  * { box-sizing: border-box; margin: 0; padding: 0; }
  html, body {
    width: 1200px; height: 900px; overflow: hidden;
    background: var(--page);
    font-family: "Open Sans", Arial, sans-serif;
  }
  .card {
    position: absolute; left: 382px;
    width: 411px; height: 248px;
    overflow: hidden;
  }
  .card--front { top: 150px; background: var(--paper); }
  .card--back  { top: 476px; background: var(--navy); }

  .brand {
    position: absolute;
    display: flex; flex-direction: column; align-items: center; justify-content: center;
    text-align: center;
  }
  .brand__dot { border-radius: 50%; background: var(--gold); }
  .brand__name { font-weight: 800; text-transform: uppercase; line-height: 1.1; }

  .card--front .brand { left: 30px; top: 52px; width: 160px; height: 140px; }
  .card--front .brand__dot { width: 34px; height: 34px; margin-bottom: 8px; }
  .card--front .brand__name { color: var(--navy); font-size: 18px; }

  .card--back .brand { left: 100px; top: 35px; width: 211px; height: 160px; }
  .card--back .brand__dot { width: 44px; height: 44px; margin-bottom: 10px; }
  .card--back .brand__name { color: var(--white); font-size: 24px; }

  .divider {
    position: absolute; left: 206px; top: 57px;
    width: 1.5px; height: 134px; background: var(--navy);
  }
  .details { position: absolute; left: 220px; top: 53px; color: var(--ink-soft); }
  .details__name { color: var(--navy); font-weight: 700; font-size: 14px; line-height: 18px; }
  .details__role { font-size: 11px; line-height: 16px; text-transform: uppercase; }
  .details__block { font-size: 11px; line-height: 16.3px; }
  .details__address { margin-top: 16px; }
  .details__contact { margin-top: 9px; }

  .band { position: absolute; left: 0; bottom: 0; width: 411px; height: 13px; }
</style>
</head>
<body>

<section class="card card--front">
  <div class="brand">
    <span class="brand__dot"></span>
    <span class="brand__name">Skyreach<br>Pacific Aerial</span>
  </div>
  <div class="divider"></div>
  <div class="details">
    <p class="details__name">HENRIK VOLLMER</p>
    <p class="details__role">Director</p>
    <div class="details__block details__address">
      <p>17 Calloway Lane</p>
      <p>Merrigum Flat, NSW 2583</p>
    </div>
    <div class="details__block details__contact">
      <p>0471 238 905 / 1300Skyreachpa</p>
      <p>info@skyreachpacificaerial.com.au</p>
      <p>www.skyreachpacificaerial.com.au</p>
    </div>
  </div>
  <svg class="band" viewBox="0 0 411 13" aria-hidden="true">
    <polygon points="0,0 210,0 197,13 0,13" fill="var(--navy)"/>
    <polygon points="217,0 411,0 411,13 204,13" fill="var(--gold)"/>
  </svg>
</section>

<section class="card card--back">
  <div class="brand">
    <span class="brand__dot"></span>
    <span class="brand__name">Skyreach<br>Pacific Aerial</span>
  </div>
  <svg class="band" viewBox="0 0 411 13" aria-hidden="true">
    <polygon points="0,0 210,0 197,13 0,13" fill="var(--paper)"/>
    <polygon points="217,0 411,0 411,13 204,13" fill="var(--gold)"/>
  </svg>
</section>

</body>
</html>
```